Non-Profit Organization Needs WordPress websiteTo Empower Women

Our client is a Non-profit organization that requires a responsively-designed WordPress website to help publish their online magazine. This website will also feature their magazine publication that they publish quarterly. The design will need to be mobile-friendly, so it looks great on all devices.

The main purpose of this site is the following, in order of importance:
1. Educate economically-challenged women to improve their lives with blog content and their online Magazine.
2. Create a Membership community for these women to help one another. THE MAIN CALL-TO-ACTION ON THE SITE IS TO MOTIVATE THE READERS TO JOIN THE FREE MEMBERSHIP COMMUNITY.
3. Recognize and Identify the contributing Organizations, and to motivate the organizations to donate money to the non-profit organization.

Here is information from the client about what they want for their website:
*********************************************************************************************
It needs to have two entrances to content: Organizations & Readers; Don't like cluttered which some magazine formats seem to be. Like edgy, yet feminine. Not sweet. Easy to navigate and find what one comes to find. Colorful.

We need: A Resources area, a Donation button prominently placed on the site, section for archived magazine articles; Place for translated issues. We will want to have a private Membership section on the site. (NOTE: These requests should be used to help create the site's navigation menu.)

Here are example websites the client likes and why. Please use them as inspiration.
http:://www.brindlewave.com color, simple design w cool buttons, uncluttered
http:://www.tolvarick.com emotion with the color, ease of getting around
http:://www.quenderpast7.com the second page has the color sections that take you to next page
http:://www.marrowlightjournal.com not sweetly feminine, perhaps community style
http:://www.pellicrest.net use of clear symbols, newer design/graphics look

Target Market(s)

The website targets 2 different audiences: Organizations that help to provide services and help to the website readers, and the Readers themselves. The Readers are mostly economically-challenged females that need inspiration and help. The Readers should be considered the Primary Target Audience, with the Organizations being secondary.

Industry/Entity Type

Non-Profit

Font styles to use
Sans Serif

Colors
f37022
fece3e

Requirements
Must have
• The final design MUST, MUST, MUST be created using Separate PSD layers for each element and graphic! PLEASE create a professional layer structure within your design, so we can code it properly.

Please do NOT use Graphics/Images where Text should be used. Examples of this are the business address, phone number, etc.

The website home page design should identify its two main audiences, the Organizations and the Readers. The main call to action is to invite the Readers to become free members of their membership community.

There MUST be an area on the home page where their online magazine can be embedded onto their site OR an image button etc that leads to the magazine. They use the http://vondrel.com/ system to create the magazine and then embed the issues on their site. Alternatively, you could create a button, image, area, etc, where the user can click the image and then go to the magazine.

A membership login field OR a button that leads to a Members login area.

A small area on the website that either Adsense or advertising can be used, and this MUST be BELOW the FOLD.

The site must project a sense of hope and/or empowerment for its Readers. The imagery should resonate with females who want to be inspired.
Nice to have
• There should be links or buttons to identify Spanish-speaking Readers and Portuguese-speaking Readers.
Should not have
• NO Gallery Sliders or Photo Sliders

```html
<!DOCTYPE html>
<html lang="en">
<head>
<meta charset="utf-8">
<title>Lift Onward — Home</title>
<link rel="stylesheet" href="https://fonts.googleapis.com/css2?family=Noto+Serif:ital,wght@0,400;0,700;1,400;1,700&display=swap">
<style>
:root{
  --orange:#f37022;
  --yellow:#fece3e;
  --yellow-deep:#f7b733;
  --cream:#fdf8ea;
  --ink:#1e1e1e;
  --text:#3a3a3a;
  --muted:#6b6b6b;
  --sky:#00aeef;
  --sky-deep:#1597d9;
  --footer:#262626;
  --footer-bar:#3a3a3a;
  --white:#ffffff;
}
*{box-sizing:border-box;margin:0;padding:0}
html,body{width:1200px;height:2579px;overflow:hidden}
body{font-family:"Noto Serif",Georgia,serif;color:var(--text);background:var(--white);position:relative}
.abs{position:absolute}

/* header */
.site-header{left:0;top:0;width:1200px;height:148px;background:var(--white)}
.brand{left:69px;top:36px;display:flex;align-items:center;gap:16px}
.brand-mark{width:70px;height:70px;background:var(--orange)}
.brand-name{font-size:58px;font-weight:700;color:var(--orange);letter-spacing:-1px;white-space:nowrap}
.cta-label{left:818px;top:42px;font-size:19px;color:var(--orange);text-transform:uppercase;white-space:nowrap}
.cta-phone{left:828px;top:66px;font-size:31px;color:var(--yellow);font-weight:700;white-space:nowrap}
.agent-photo{left:1040px;top:9px;width:86px;height:90px;border-radius:4px;background:linear-gradient(#e9d9c8,#5a4a40)}
.search{left:818px;top:101px;width:313px;height:35px;border:2px solid var(--yellow);display:flex}
.search span{flex:1;font-size:12px;color:#bbb;padding:9px 10px}
.search i{width:35px;background:var(--yellow);display:flex;align-items:center;justify-content:center}

/* nav */
.main-nav{left:0;top:148px;width:1200px;height:57px;background:var(--yellow);border-bottom:3px solid var(--yellow-deep)}
.main-nav ul{list-style:none;position:absolute;left:69px;top:0;display:flex;height:57px}
.main-nav li{height:57px;display:flex;align-items:center;justify-content:center;font-size:17px;color:var(--ink);border-right:1px solid rgba(0,0,0,.12);white-space:nowrap}
.main-nav .current{background:var(--orange);color:var(--white)}
.main-nav .member{background:var(--yellow-deep);font-style:italic;font-weight:700}
.main-nav .donate{background:var(--orange);color:var(--white);font-style:italic;font-weight:700}

/* hero */
.hero{left:0;top:205px;width:1200px;height:550px;background:radial-gradient(ellipse at 50% 25%,#b9a999 0%,#5c5650 45%,#1d1d1d 100%)}
.hero-title{left:0;top:322px;width:1200px;text-align:center;color:var(--white);font-size:33px;font-weight:700;line-height:43px;text-transform:uppercase}
.hero-rule{left:215px;top:424px;width:770px;height:1px;background:rgba(255,255,255,.4)}
.hero-btn{top:448px;height:52px;display:flex;align-items:center;justify-content:center;font-size:21px;font-style:italic;font-weight:700;white-space:nowrap}
.btn-solid{background:var(--yellow);color:var(--ink)}
.btn-ghost{border:2px solid rgba(255,255,255,.45);color:var(--yellow);background:rgba(0,0,0,.3)}

/* tiles */
.tile{top:798px;width:330px;height:177px;display:flex;align-items:center;justify-content:center}
.tile-frame{position:absolute;left:12px;top:12px;right:12px;bottom:12px;border:3px solid rgba(255,255,255,.7)}
.tile-label{position:relative;font-size:30px;font-weight:700;white-space:nowrap}

/* help */
.help{left:0;top:1018px;width:1200px;height:374px;background:var(--yellow)}
.help h2{left:69px;top:52px;font-size:33px;color:var(--ink)}
.help p{left:69px;top:108px;width:500px;font-size:13.5px;line-height:27px;color:var(--ink)}
.video{left:600px;top:32px;width:531px;height:311px;background:linear-gradient(135deg,#3b3b3b,#7a7068 55%,#2c2c2c)}
.video-bar{left:0;bottom:0;width:531px;height:38px;background:#1b1b1b;color:#ccc;font-size:11px;display:flex;align-items:center;gap:14px;padding:0 14px}

/* blog */
.blog-title{left:69px;top:1415px;font-size:33px;font-weight:700;color:var(--orange)}
.blog-card{left:69px;top:1470px;width:677px;height:320px;background:var(--cream);border:1px solid #eee0c0}
.blog-photo{left:0;top:0;width:333px;height:318px;background:linear-gradient(#c7b48e,#5a3b2b)}
.blog-body{left:352px;top:24px;width:300px}
.blog-body h3{font-size:19px;color:var(--orange);font-weight:700;margin-bottom:14px}
.blog-body h4{font-size:16px;font-style:italic;font-weight:700;color:var(--ink);margin-bottom:14px}
.blog-body h5{font-size:14px;font-style:italic;font-weight:400;color:var(--ink);margin-bottom:6px}
.blog-body p{font-size:13px;line-height:23px;color:var(--muted)}
.read-more{display:inline-block;margin-top:22px;background:var(--orange);color:var(--white);font-size:12px;font-style:italic;padding:6px 14px}
.archive{left:753px;top:1470px;width:378px;height:320px;background:var(--cream);border:1px solid #eee0c0}
.archive h3{left:52px;top:18px;font-size:22px;color:var(--orange)}
.archive-item{left:55px;width:300px;height:76px}
.archive-img{left:0;top:0;width:237px;height:76px;background:linear-gradient(#8a7a6c,#2f2a26)}
.archive-img span{position:absolute;left:8px;bottom:4px;font-size:12px;font-style:italic;color:var(--yellow);white-space:nowrap}
.archive-date{left:240px;top:0;width:60px;height:76px;background:var(--yellow);text-align:center;color:var(--ink);font-weight:700;font-size:26px;line-height:30px;padding-top:6px}
.archive-date small{display:block;font-size:19px}

/* social */
.social{left:0;top:1834px;width:1200px;height:449px;background:linear-gradient(#19a6e6,#1f8fd6)}
.social-top{left:0;top:0;width:1200px;height:91px;background:var(--sky)}
.social-name{left:0;top:20px;width:1200px;text-align:center;color:var(--white);font-size:17px;font-weight:700}
.circle{top:35px;width:120px;height:120px;border-radius:50%;background:var(--white);border:6px solid var(--sky-deep)}
.circle-dot{position:absolute;left:30px;top:30px;width:48px;height:48px;border-radius:50%;background:var(--sky)}
.handle{left:514px;top:67px;width:174px;height:47px;background:var(--sky);border:3px solid var(--sky-deep);color:var(--white);font-size:15px;font-style:italic;font-weight:700;display:flex;align-items:center;justify-content:center}
.quote{left:70px;top:178px;width:1060px;text-align:center;color:var(--white);font-size:19px;font-style:italic;line-height:33px}
.ago{left:0;top:298px;width:1200px;text-align:center;color:var(--white);font-size:15px}
.ago-line{top:308px;width:74px;height:1px;background:rgba(255,255,255,.7)}
.stat{top:343px;width:120px;text-align:center;color:var(--white)}
.stat b{display:block;font-size:20px;margin-bottom:8px}
.stat span{display:block;background:var(--white);color:var(--ink);font-size:17px;font-style:italic;height:36px;line-height:36px}

/* footer */
.footer{left:0;top:2283px;width:1200px;height:235px;background:var(--footer);color:#ddd}
.footer h4{font-size:19px;font-weight:400;color:var(--yellow)}
.footer-menu{left:69px;top:20px}
.footer-menu ul{list-style:none;margin-top:16px;font-size:14.5px;line-height:26px}
.footer-menu .current{color:var(--orange)}
.footer-sep{top:0;width:1px;height:210px;background:#333}
.newsletter{left:387px;top:20px;width:310px}
.newsletter p{font-size:14.5px;line-height:24px;margin-top:14px}
.subscribe{margin-top:16px;display:flex;height:34px}
.subscribe span{width:190px;background:#1a1a1a;color:#777;font-size:13px;font-style:italic;padding:8px 10px 0 48px}
.subscribe b{background:var(--yellow);color:var(--ink);font-size:13px;font-style:italic;padding:9px 10px}
.socials{display:flex;gap:12px;margin-top:16px}
.socials i{width:42px;height:42px;border-radius:50%;border:2px solid #555;display:block}
.contact{left:896px;top:20px;width:250px}
.contact dl{margin-top:16px;font-size:14px;line-height:22px}
.contact dt{color:var(--yellow);font-style:italic}
.contact dd{margin-bottom:12px}
.footer-bar{left:0;top:2518px;width:1200px;height:61px;background:var(--footer-bar);color:#bbb;font-size:13px}
.footer-bar .copy{left:69px;top:22px}
.footer-bar .links{right:69px;top:22px}
</style>
</head>
<body>

<header class="abs site-header">
  <div class="abs brand"><span class="brand-mark"></span><span class="brand-name">Lift Onward</span></div>
  <div class="abs cta-label">Call to action on</div>
  <div class="abs cta-phone">555 014 2270</div>
  <div class="abs agent-photo" role="img" aria-label="Support agent wearing a headset"></div>
  <div class="abs search"><span>Search</span><i>
    <svg width="18" height="18" viewBox="0 0 18 18"><circle cx="7.5" cy="7.5" r="5.5" fill="none" stroke="#fff" stroke-width="2"/><line x1="11.5" y1="11.5" x2="16" y2="16" stroke="#fff" stroke-width="2.5"/></svg></i></div>
</header>

<nav class="abs main-nav">
  <ul>
    <li class="current" style="width:99px">Home</li>
    <li style="width:124px">About Us</li>
    <li style="width:194px">Online Magazine</li>
    <li style="width:150px">Case Studies</li>
    <li style="width:88px">Blog</li>
    <li style="width:158px">Contact Us</li>
    <li class="member" style="width:155px">Member Login</li>
    <li class="donate" style="width:95px">Donate</li>
  </ul>
</nav>

<section class="abs hero" role="img" aria-label="Smiling woman with glasses in a bright office">
  <h1 class="abs hero-title">The main motivate the readers to woman<br>join the free membership community.</h1>
  <div class="abs hero-rule"></div>
  <a class="abs hero-btn btn-solid" style="left:215px;width:208px">Member Login</a>
  <a class="abs hero-btn btn-ghost" style="left:456px;width:262px">Donate Lift Onward</a>
  <a class="abs hero-btn btn-ghost" style="left:750px;width:235px">Online Magazine</a>
</section>

<a class="abs tile" style="left:69px;background:linear-gradient(#a8a29a,#5c5852)" role="img" aria-label="Woman reading the magazine on a laptop">
  <span class="tile-frame" style="background:rgba(255,255,255,.55);border-color:rgba(255,255,255,.3)"></span>
  <span class="tile-label" style="color:var(--ink);font-weight:400">online Magazine</span>
</a>
<a class="abs tile" style="left:435px;background:linear-gradient(#3e3a36,#1b1a19)" role="img" aria-label="Open cupped hands offering help">
  <span class="tile-frame"></span>
  <span class="tile-label" style="color:var(--yellow);font-size:27px">Donate Lift Onward</span>
</a>
<a class="abs tile" style="left:801px;background:linear-gradient(#6a4a38,#201915)" role="img" aria-label="Smiling woman wearing a headset">
  <span class="tile-frame"></span>
  <span class="tile-label" style="color:var(--yellow)">CAll TO Action</span>
</a>

<section class="abs help">
  <h2 class="abs">How Can You Help?</h2>
  <p class="abs">Lorem ipsum dolor sit amet, consectetur adipiscing elit. Curabitur hendrerit egestas metus, nec fringilla dolor at. Nam malesuada, dui non rhoncus laoreet, ligula quam dictum ipsum, a rhoncus lectus dolor comm us. Maecenas feugiat mattis blandit. Praesent mattis ligula a gravida faucibus. Morbi est eros, mattis sit amet massa ut, vultate dignissim nisi. Maecenas ac leo dui. Vestibulum eu fringilla sapien. Nulla porta, augue vitae tempus cursus, erat odio faucibus elit, a laoreet mauris erat id velit. Donec nulla ntum consectetur tortor.</p>
  <div class="abs video" role="img" aria-label="Video of two women talking at an office desk">
    <svg class="abs" style="left:235px;top:112px" width="62" height="62" viewBox="0 0 62 62"><circle cx="31" cy="31" r="28" fill="rgba(0,0,0,.25)" stroke="#fece3e" stroke-width="4"/><polygon points="25,19 45,31 25,43" fill="#fece3e"/></svg>
    <div class="abs video-bar"><span>▶</span><span>0:00 / 2:58</span></div>
  </div>
</section>

<h2 class="abs blog-title">Latest from Our Blog</h2>
<article class="abs blog-card">
  <div class="abs blog-photo" role="img" aria-label="Group of smiling children outdoors"></div>
  <div class="abs blog-body">
    <h3>Lorem ipsum dolor sit amet</h3>
    <h4>Consectetur adipiscing elit</h4>
    <h5>Proin ultricies nunc vel consectetur</h5>
    <p>Sed ornare semper magna ac pretium. Cum sociis natoque penatibus et magnis dis parturient montes, nascetur ridiculus mus. Sed sodales dui id velit rhoncus tincidunt. dolor odio</p>
    <span class="read-more">Read more</span>
  </div>
</article>
<aside class="abs archive">
  <h3 class="abs">Blog Aechive</h3>
  <div class="abs archive-item" style="top:58px"><div class="abs archive-img" role="img" aria-label="Woman at a desk"><span>Lorem ipsum dolor sit amet</span></div><div class="abs archive-date">19<small>Jun</small></div></div>
  <div class="abs archive-item" style="top:140px"><div class="abs archive-img" role="img" aria-label="Group of children"><span>Lorem ipsum dolor sit amet</span></div><div class="abs archive-date">21<small>Jun</small></div></div>
  <div class="abs archive-item" style="top:222px"><div class="abs archive-img" role="img" aria-label="Open hands"><span>Lorem ipsum dolor sit amet</span></div><div class="abs archive-date">25<small>Jun</small></div></div>
</aside>

<section class="abs social">
  <div class="abs social-top"></div>
  <div class="abs social-name">Lorem ispum</div>
  <div class="abs circle" style="left:325px"><span class="circle-dot"></span></div>
  <div class="abs circle" style="left:757px;background:linear-gradient(#d9b79a,#3a3a3a)" role="img" aria-label="Profile portrait"></div>
  <div class="abs handle">@Lorem ispum</div>
  <p class="abs quote">Lorem ipsum dolor sit amet, consectetur adipiscing elit. Proin ultricies nunc vel consectetur vestibulum. Sed ornare semper magna ac pretium. Cum sociis natoque penatibus et magnis dis parturient montes, nascetur ridiculus mus. Sed sodales dui id velit rhoncus tincidunt. Mauris vel molestie tortor.</p>
  <div class="abs ago">13 hours ago</div>
  <div class="abs ago-line" style="left:468px"></div>
  <div class="abs ago-line" style="left:660px"></div>
  <div class="abs stat" style="left:399px"><b>7540</b><span>Tweets</span></div>
  <div class="abs stat" style="left:542px"><b>950</b><span>Following</span></div>
  <div class="abs stat" style="left:684px"><b>54586</b><span>Followers</span></div>
</section>

<footer class="abs footer">
  <div class="abs footer-menu">
    <h4>Menu</h4>
    <ul><li class="current">Home</li><li>About Us</li><li>Online Magazine</li><li>Case Studies</li><li>Blog</li><li>Contact Us</li></ul>
  </div>
  <div class="abs footer-sep" style="left:275px"></div>
  <div class="abs newsletter">
    <h4>Subscribe to Our Newsletter</h4>
    <p>Lorem ipsum dolor sit amet, con adipiscing elit. Aliquam</p>
    <div class="subscribe"><span>your@email.com</span><b>SUBSCRIBE</b></div>
    <div class="socials"><i></i><i></i><i></i><i></i><i></i></div>
  </div>
  <div class="abs footer-sep" style="left:798px"></div>
  <div class="abs contact">
    <h4>Get In Touch</h4>
    <dl>
      <dt>Address:</dt><dd>Lorem ipsum dolor sit amet , conser adipiscing elit. Aen ligula</dd>
      <dt>Phone: <span style="color:#ddd;font-style:normal">+1 555 014 2271</span></dt><dd></dd>
      <dt>Email: <span style="color:#ddd;font-style:normal">info@liftonward.org</span></dt>
    </dl>
  </div>
</footer>
<div class="abs footer-bar">
  <span class="abs copy">Copyright © 2014 Lift Onward. All rights reserved.</span>
  <span class="abs links">Sitemap &nbsp;/&nbsp; Terms of Use &nbsp;/&nbsp; Privacy</span>
</div>

</body>
</html>
```